Introducing a Personal Care Product called" ORBA"

We are a nutra-pharmaceutical company launching a new personal care product called ORBA. Some of the products include massage and aroma therapy, as well as personal lubricants. The products will be produced and put into, two bottles that are interlocking so two combinations of products can be purchased at once (i.e. massage and aroma therapy). The poster will be used for promotional advertising, trade shows and for in-store promotions.
Updates

We would like to see a design without the product.

Target Market(s)

Products will be aimed at adults primarily women 18-65 in the USA. We want to appeal to the everyday woman who is interested in their sexual well being.

Industry/Entity Type

Massage

Requirements
Must have
• Clean Presentation. Not many colors. Text should be as follows: ORBA for Her....ORBA for Him...ORBA for You...Let's ORBA see attached..Also ORBA with Her...Orba with Him..Let's ORBA..Open to other copy versions.
Nice to have
• Product image not necessary but can be used. image attached
Should not have
• Too many colors...

```html
<!DOCTYPE html>
<html lang="en">
<head>
<meta charset="utf-8">
<title>ORBA for You – Poster</title>
<link rel="stylesheet" href="https://fonts.googleapis.com/css2?family=Lato:wght@300;700&display=swap">
<style>
  :root {
    --page-bg: #ececec;
    --poster-grey: #d6d6d8;
    --poster-glow: #ffffff;
    --her-pink: #f3a9bd;
    --her-deep: #d8456f;
    --him-blue: #a9dcf3;
    --him-deep: #27a3dd;
    --you-grey: #9a9a9c;
    --band-pink: #f3afc2;
    --white: #ffffff;
  }
  * { box-sizing: border-box; margin: 0; padding: 0; }
  html, body {
    width: 1200px;
    height: 1200px;
    overflow: hidden;
    background: var(--page-bg);
    font-family: "Lato", Arial, sans-serif;
  }
  .poster {
    position: absolute;
    left: 200px;
    top: 40px;
    width: 800px;
    height: 1120px;
    overflow: hidden;
    background: radial-gradient(ellipse 52% 46% at 50% 55%, var(--poster-glow) 0%, var(--poster-glow) 55%, var(--poster-grey) 100%);
  }
  .symbols {
    position: absolute;
    inset: 0;
    width: 800px;
    height: 1120px;
  }
  .headline {
    position: absolute;
    font-size: 50px;
    line-height: 1;
    white-space: nowrap;
    letter-spacing: -0.5px;
  }
  .headline b { font-weight: 700; }
  .headline span { font-weight: 300; }
  .headline--her { left: 38px; top: 170px; }
  .headline--her b { color: var(--her-deep); }
  .headline--her span { color: var(--her-deep); opacity: 0.85; }
  .headline--him { left: 340px; top: 218px; }
  .headline--him b { color: var(--him-deep); }
  .headline--him span { color: var(--him-deep); opacity: 0.85; }
  .product-shot {
    position: absolute;
    left: 210px;
    top: 380px;
    width: 400px;
    height: 480px;
    border-radius: 18px;
    background:
      linear-gradient(90deg, rgba(214,76,110,0.35) 0%, rgba(243,169,189,0.45) 48%, rgba(169,220,243,0.55) 52%, rgba(39,163,221,0.35) 100%),
      linear-gradient(180deg, #e9e9ec 0%, #f6f6f8 100%);
  }
  .tagline-you {
    position: absolute;
    left: 330px;
    top: 900px;
    font-size: 46px;
    color: var(--you-grey);
    white-space: nowrap;
  }
  .tagline-you b { font-weight: 700; }
  .tagline-you span { font-weight: 300; }
  .band {
    position: absolute;
    left: 0;
    bottom: 0;
    width: 100%;
    height: 150px;
    background: linear-gradient(180deg, rgba(243,175,194,0.55) 0%, rgba(243,175,194,0.55) 52%, var(--band-pink) 52%);
  }
  .band-cta {
    position: absolute;
    right: 36px;
    top: 18px;
    font-size: 48px;
    color: var(--white);
    white-space: nowrap;
  }
  .band-cta span { font-weight: 300; }
  .band-cta b { font-weight: 700; }
</style>
</head>
<body>
  <main class="poster">
    <svg class="symbols" viewBox="0 0 800 1120" aria-hidden="true">
      <g class="venus" fill="none" stroke="var(--her-pink)" stroke-width="22">
        <circle cx="250" cy="190" r="108"/>
        <line x1="250" y1="298" x2="250" y2="420"/>
        <line x1="180" y1="352" x2="320" y2="352"/>
      </g>
      <g class="mars" fill="none" stroke="var(--him-blue)" stroke-width="22">
        <circle cx="520" cy="238" r="130"/>
        <line x1="612" y1="146" x2="740" y2="18"/>
        <polyline points="640,8 750,8 750,118"/>
      </g>
    </svg>

    <h1 class="headline headline--her"><b>Orba</b> <span>for Her</span></h1>
    <h2 class="headline headline--him"><b>Orba</b> <span>for Him</span></h2>

    <div class="product-shot" role="img" aria-label="Photo of two interlocking ORBA bottles: a red-capped lubricant for her and a blue-capped lubricant for him"></div>

    <p class="tagline-you"><b>Orba</b> <span>for you</span></p>

    <div class="band">
      <p class="band-cta"><span>Let's</span> <b>Orba</b></p>
    </div>
  </main>
</body>
</html>
```